Brightwell Acupuncture Studio Website Design

We are working with Brightwell Acunpuncture Studio. They are a local Chinese medicine and acupuncture studio and in need of a new website design.

Some sites to use for inspiration:

https://marbleriveracupuncture.example
https://cedarglowacupuncture.example
https://quietharborclinic.example
https://emberfieldacupuncture.example
https://fernhollowclinic.example

Thank you for taking the time to consider designing a website for us. We are web developers based in Stockton, CA, USA. Most of our projects go through the same process. Understanding this process may help you win a project with us. We custom-code all of our websites in-house. We don’t have any requirements as to what tools you use for your design, but we prefer Figma files. For any design that we label as four-stars, we send it to the client for review. The client picks the final design they want us to use. Once we complete this process, we will continue to show additional clients all the four-star sites and purchase them later. Your designs will have multiple chances to sell. For better chances of success, we ask that you follow these guidelines.

IMAGES:
If you use any images or icons in the design, we ask that you have a link to the asset so we can purchase the image/icon. Most of the designs we submit do not have the customer’s images on them unless they have some great images. Be creative; show us the feeling you are trying to portray with your image choices. Use any royalty-free site you choose. We subscribe to Vantrel and mainly use their images, but we can purchase images outside of Vantrel.

PLEASE NOTE: we will not submit designs to clients with watermarks on the images.

FONTS:
We ask that you identify the fonts used in the design. This can be done in a message if you want. We typically use Google Fonts and Vantrel Fonts.

CONTENT:
We're always open to different content and ideas. We often submit designs with stock images so the client can see our vision. We typically take pictures after the website launch to use their images with our vision. Lorem Ipsum is fine for paragraphs, but we ask that you write the headers in correct English. We want to be able to show the vision and identify the sections of the website.

INSPIRATION:
We typically add a couple of links in the brief of websites we like to help you get started in your design.

REVISIONS:
We do not often ask for revisions of the designs unless we see something in the design that may not appeal to the client. If there are slight changes that we want to make, we do that in the development process.

FEEDBACK:
We rarely give feedback on designs during the design process. We are working on many website projects and do not have the time to provide feedback. We usually respond if your request is well thought out and asks specific questions, but a note asking “feedback, please” usually goes unanswered.

```html
<!DOCTYPE html>
<html lang="en">
<head>
<meta charset="utf-8">
<title>Brightwell Acupuncture Studio</title>
<link href="https://fonts.googleapis.com/css2?family=Montserrat:wght@400;500;600;700&display=swap" rel="stylesheet">
<style>
:root{
  --ink:#262d38;
  --ink-2:#2f3744;
  --coral:#e0685a;
  --coral-soft:#e8887c;
  --paper:#ffffff;
  --muted:#8a8f98;
  --text:#3b3f46;
  --line:#e3e3e3;
}
*{box-sizing:border-box;margin:0;padding:0}
html,body{width:1200px;height:3748px;overflow:hidden}
body{font-family:"Montserrat",Arial,sans-serif;color:var(--text);background:var(--paper);position:relative}
section,header,footer{position:absolute;left:0;width:1200px}
.btn{position:absolute;display:inline-block;background:var(--coral);color:#fff;font-size:13px;font-weight:600;text-transform:uppercase;letter-spacing:.5px;padding:12px 24px;border-radius:24px}
.brand{display:flex;align-items:center;gap:10px;font-weight:700;font-size:22px;line-height:1.05}
.brand-dot{width:14px;height:14px;border-radius:50%;background:var(--coral)}
.photo{position:absolute}

/* hero */
.hero{top:0;height:820px;background:var(--ink)}
.hero .photo{inset:0;background:linear-gradient(100deg,#2a2622 0%,#4a3f37 45%,#8a7566 75%,#b69c88 100%)}
.hero .shade{position:absolute;inset:0;background:linear-gradient(90deg,rgba(30,34,42,.75) 0%,rgba(30,34,42,.35) 60%,rgba(30,34,42,.15) 100%)}
.menu-btn{position:absolute;left:60px;top:36px;border:1px solid rgba(255,255,255,.6);color:#fff;font-size:12px;padding:8px 16px;border-radius:20px;display:flex;gap:8px;align-items:center}
.hero .brand{position:absolute;left:50%;top:28px;transform:translateX(-50%);color:#fff}
.hero .btn-top{right:60px;top:32px}
.hero h1{position:absolute;left:60px;top:400px;color:#fff;font-size:60px;font-weight:600;line-height:1.1}
.hero p{position:absolute;left:60px;top:572px;width:500px;color:#fff;font-size:14px;line-height:1.6}
.hero .btn-main{right:60px;top:576px}
.scroll-ring{position:absolute;right:70px;top:400px}

/* intro */
.intro{top:820px;height:560px;background:var(--ink)}
.intro h2{position:absolute;left:60px;top:60px;width:330px;color:#fff;font-size:40px;font-weight:600;line-height:1.15}
.intro .photo{left:500px;top:-60px;width:280px;height:400px;background:linear-gradient(160deg,#d9d2cc,#a39a93 60%,#5f5750)}
.intro p{position:absolute;left:820px;top:20px;width:340px;color:#d7dae0;font-size:13px;line-height:1.7}
.stats{position:absolute;left:60px;top:390px;width:1080px;display:flex;justify-content:space-around;padding-top:20px}
.stat{text-align:center}
.stat b{display:block;color:var(--coral);font-size:44px;font-weight:600}
.stat span{color:#c9ccd2;font-size:13px}

/* services */
.services{top:1380px;height:520px;background:var(--paper)}
.services h2{position:absolute;left:60px;top:100px;color:var(--ink);font-size:40px;font-weight:600;line-height:1.1}
.services .arrows{position:absolute;left:60px;top:236px;display:flex;gap:18px}
.services .lead{position:absolute;left:60px;top:290px;width:230px;font-size:12px;line-height:1.6;color:var(--muted)}
.services .btn{left:60px;top:400px}
.card{position:absolute;top:48px;width:228px}
.card .photo{position:static;height:232px}
.card h3{margin-top:16px;font-size:16px;font-weight:600;color:var(--ink)}
.card p{margin-top:8px;font-size:12px;line-height:1.6;color:var(--muted)}
.card a{display:block;margin-top:10px;font-size:12px;color:var(--coral);font-weight:600;text-decoration:none}

/* east west */
.eastwest{top:1900px;height:740px;background:var(--ink)}
.eastwest h2{position:absolute;left:60px;top:64px;color:#fff;font-size:40px;font-weight:600;line-height:1.25}
.feature{position:absolute;width:240px;color:#fff}
.feature h3{display:flex;gap:10px;align-items:center;color:var(--coral);font-size:15px;font-weight:600}
.feature p{margin-top:10px;font-size:12px;line-height:1.6;color:#c9ccd2}
.eastwest .photo{left:600px;top:0;width:600px;height:560px;background:linear-gradient(135deg,#cbbfb6,#e8dfd8 45%,#b59f90)}
.healthy{position:absolute;left:600px;top:520px;width:600px;height:220px;background:linear-gradient(180deg,rgba(224,104,90,0) 0%,var(--coral) 22%);padding:16px 40px 0}
.healthy h3{color:#fff;font-size:30px;font-weight:600;margin-top:-12px}
.healthy p{color:#fff;font-size:12px;line-height:1.65;margin-top:18px;width:480px}

/* testimonials */
.reviews{top:2640px;height:480px;background:var(--paper)}
.reviews h2{position:absolute;left:60px;top:80px;color:var(--ink);font-size:38px;font-weight:600}
.quote{position:absolute;top:170px;width:500px}
.quote p{font-size:13px;line-height:1.7;color:var(--muted)}
.person{display:flex;gap:14px;align-items:center;margin-top:30px}
.avatar{width:52px;height:52px;border-radius:50%;background:linear-gradient(135deg,#e8cdb8,#b98d6f)}
.person b{display:block;color:var(--ink);font-size:14px}
.stars{color:var(--coral);font-size:13px;letter-spacing:2px}

/* cta */
.cta{top:3120px;height:340px;background:var(--ink)}
.cta .photo{inset:0;background:linear-gradient(90deg,#3a3531,#5b5148 55%,#7c6f64)}
.cta .shade{position:absolute;inset:0;background:rgba(30,34,42,.55)}
.cta h2{position:absolute;left:0;width:1200px;top:96px;text-align:center;color:#fff;font-size:40px;font-weight:600}
.cta p{position:absolute;left:300px;width:600px;top:160px;text-align:center;color:#e4e4e4;font-size:13px;line-height:1.6}
.cta .btn{left:50%;transform:translateX(-50%);top:240px}

/* footer */
.site-footer{top:3460px;height:288px;background:var(--paper)}
.site-footer .brand{position:absolute;left:60px;top:56px;color:var(--ink)}
.fcol{position:absolute;top:56px}
.fcol h4{color:var(--ink);font-size:15px;font-weight:600;margin-bottom:14px}
.fcol li{list-style:none;font-size:12px;color:var(--muted);line-height:2}
.socials{position:absolute;left:60px;top:140px;display:flex;gap:10px}
.socials span{width:26px;height:26px;border-radius:50%;background:var(--coral)}
.legal{position:absolute;left:60px;top:238px;width:1080px;border-top:1px solid var(--line);padding-top:18px;display:flex;justify-content:space-between;font-size:11px;color:var(--muted)}
</style>
</head>
<body>

<header class="hero">
  <div class="photo" role="img" aria-label="Acupuncturist placing a needle on a relaxed client's forehead"></div>
  <div class="shade"></div>
  <div class="menu-btn">
    <svg width="14" height="10" viewBox="0 0 14 10"><path d="M0 1h14M0 5h14M0 9h14" stroke="#fff" stroke-width="1.5"/></svg>Menu
  </div>
  <div class="brand"><span class="brand-dot"></span><span>Brightwell<br>Acupuncture Studio</span></div>
  <span class="btn btn-top">Enquire now</span>
  <h1>Personalized Care.<br>Powerful Results.</h1>
  <p>With treatments built around your individual needs, luxury, and high attention, you're in the right place if you are looking for acupuncture, cupping, or Reiki energy healing you will find it here.</p>
  <svg class="scroll-ring" width="110" height="110" viewBox="0 0 110 110" aria-hidden="true">
    <circle cx="55" cy="55" r="48" fill="none" stroke="rgba(255,255,255,.4)"/>
    <circle cx="55" cy="55" r="20" fill="none" stroke="var(--coral)" stroke-width="1.5"/>
    <path d="M55 46v18M49 58l6 6 6-6" stroke="var(--coral)" stroke-width="1.5" fill="none"/>
  </svg>
  <span class="btn btn-main">Enquire now</span>
</header>

<section class="intro">
  <h2>You are here because you are ready to feel better acupuncture can help.</h2>
  <div class="photo" role="img" aria-label="Practitioner treating a pregnant client's shoulder"></div>
  <p>Lorem Ipsum is simply dummy text of the printing and typesetting industry. Lorem Ipsum has been the industry's standard dummy text ever since the 1500s, when an unknown printer took a galley of type and scrambled it to make a type specimen book. It has survived not only five centuries, but also the leap into electronic typesetting, remaining essentially unchanged. It was popularised in the 1960s with the release of Letraset sheets containing Lorem Ipsum passages, and more recently with desktop publishing software.</p>
  <div class="stats">
    <div class="stat"><b>15+</b><span>Years of Experience</span></div>
    <div class="stat"><b>200+</b><span>Tailored Treatment Plans</span></div>
    <div class="stat"><b>5+</b><span>Different Countries Served</span></div>
  </div>
</section>

<section class="services">
  <h2>Our<br>Services</h2>
  <div class="arrows">
    <svg width="24" height="12" viewBox="0 0 24 12"><path d="M24 6H2M7 1L2 6l5 5" stroke="var(--coral)" stroke-width="1.5" fill="none"/></svg>
    <svg width="24" height="12" viewBox="0 0 24 12"><path d="M0 6h22M17 1l5 5-5 5" stroke="var(--muted)" stroke-width="1.5" fill="none"/></svg>
  </div>
  <p class="lead">Lorem Ipsum is simply dummy text of the printing and typesetting industry. Lorem Ipsum has been the industry's standard dummy text.</p>
  <span class="btn">Discover More</span>

  <article class="card" style="left:340px">
    <div class="photo" role="img" aria-label="Acupuncture needles on a client's back" style="background:linear-gradient(150deg,#e9d6c8,#c79e84)"></div>
    <h3>Acupuncture</h3>
    <p>Lorem Ipsum is simply dummy text of the printing and typesetting industry.</p>
    <a>Learn More ›</a>
  </article>
  <article class="card" style="left:608px">
    <div class="photo" role="img" aria-label="Microneedling facial treatment" style="background:linear-gradient(150deg,#e4e1df,#a9a3a0)"></div>
    <h3>Microneedling</h3>
    <p>Lorem Ipsum is simply dummy text of the printing and typesetting industry.</p>
    <a>Learn More ›</a>
  </article>
  <article class="card" style="left:876px">
    <div class="photo" role="img" aria-label="Fire cupping glasses on a client's back" style="background:linear-gradient(150deg,#d9b48a,#6e4b33)"></div>
    <h3>Fire Cupping</h3>
    <p>Lorem Ipsum is simply dummy text of the printing and typesetting industry.</p>
    <a>Learn More ›</a>
  </article>
  <article class="card" style="left:1144px">
    <div class="photo" role="img" aria-label="Relaxing spa treatment" style="background:linear-gradient(150deg,#e6cbb6,#a67c62)"></div>
    <h3>Reiki</h3>
    <p>Lorem Ipsum is simply dummy text of the printing and typesetting industry.</p>
    <a>Learn More ›</a>
  </article>
</section>

<section class="eastwest">
  <h2>East + West<br>=<br>Brightwell Acupuncture</h2>
  <div class="feature" style="left:60px;top:330px">
    <h3><svg width="18" height="18" viewBox="0 0 18 18"><path d="M2 9c3-5 11-5 14 0-3 5-11 5-14 0z" fill="none" stroke="var(--coral)" stroke-width="1.5"/><circle cx="9" cy="9" r="2" fill="var(--coral)"/></svg>Listen</h3>
    <p>Lorem Ipsum is simply dummy text of the printing and typesetting industry.</p>
  </div>
  <div class="feature" style="left:340px;top:330px">
    <h3><svg width="18" height="18" viewBox="0 0 18 18"><path d="M2 4h6l1 2 1-2h6v11h-6l-1 1-1-1H2z" fill="none" stroke="var(--coral)" stroke-width="1.5"/></svg>Educate</h3>
    <p>Lorem Ipsum is simply dummy text of the printing and typesetting industry.</p>
  </div>
  <div class="feature" style="left:60px;top:500px">
    <h3><svg width="18" height="18" viewBox="0 0 18 18"><path d="M9 16S2 11 2 6a3.5 3.5 0 0 1 7-1 3.5 3.5 0 0 1 7 1c0 5-7 10-7 10z" fill="none" stroke="var(--coral)" stroke-width="1.5"/></svg>Heal</h3>
    <p>Lorem Ipsum is simply dummy text of the printing and typesetting industry.</p>
  </div>
  <div class="feature" style="left:340px;top:500px">
    <h3><svg width="18" height="18" viewBox="0 0 18 18"><path d="M2 11l4 4h6l4-5-3-1-2 2M2 11l5-5 4 2" fill="none" stroke="var(--coral)" stroke-width="1.5"/></svg>Support</h3>
    <p>Lorem Ipsum is simply dummy text of the printing and typesetting industry.</p>
  </div>
  <div class="photo" role="img" aria-label="Smiling client during a facial acupuncture session"></div>
  <div class="healthy">
    <h3>Get back to your healthy Self</h3>
    <p>Lorem Ipsum is simply dummy text of the printing and typesetting industry. Lorem Ipsum has been the industry's standard dummy text ever since the 1500s, when an unknown printer took a galley of type and scrambled it to make a type specimen book. It has survived not only five centuries, but also the leap into electronic typesetting, remaining essentially unchanged.</p>
  </div>
</section>

<section class="reviews">
  <h2>What Our Patients Are Says...</h2>
  <div class="quote" style="left:60px">
    <p>“Lorem Ipsum is simply dummy text of the printing and typesetting industry. Lorem Ipsum has been the industry's standard dummy text ever since the 1500s, when an unknown printer took a galley of type and scrambled it to make a type specimen book. It has survived not only five centuries, but also the leap into electronic typesetting, remaining essentially unchanged. It was popularised in the 1960s with the release of Letraset sheets containing.”</p>
    <div class="person"><div class="avatar" role="img" aria-label="Patient portrait"></div><div><b>Dana</b><span class="stars">★★★★★</span></div></div>
  </div>
  <div class="quote" style="left:640px">
    <p>“Lorem Ipsum is simply dummy text of the printing and typesetting industry. Lorem Ipsum has been the industry's standard dummy text ever since the 1500s, when an unknown printer took a galley of type and scrambled it to make a type specimen book. It has survived not only five centuries, but also the leap into electronic typesetting, remaining essentially unchanged. It was popularised in the 1960s with the release of Letraset sheets containing.”</p>
    <div class="person"><div class="avatar" role="img" aria-label="Patient portrait"></div><div><b>Dana</b><span class="stars">★★★★★</span></div></div>
  </div>
</section>

<section class="cta">
  <div class="photo" role="img" aria-label="Calm treatment room with candles and stones"></div>
  <div class="shade"></div>
  <h2>Ready to Feel Better?</h2>
  <p>Lorem Ipsum is simply dummy text of the printing and typesetting industry. Lorem Ipsum has been the industry's standard dummy text ever since the 1500s, when an unknown printer took a galley of type and scrambled it to make a type specimen book.</p>
  <span class="btn">Enquire now</span>
</section>

<footer class="site-footer">
  <div class="brand"><span class="brand-dot"></span><span>Brightwell<br>Acupuncture Studio</span></div>
  <div class="socials"><span></span><span></span><span></span></div>
  <div class="fcol" style="left:340px"><h4>Navigation</h4><ul><li>About</li><li>What to Expect</li><li>Fees</li><li>Shop</li><li>Contact</li></ul></div>
  <div class="fcol" style="left:610px"><h4>Contact</h4><ul><li>(555) 014-2287</li><li>hello@brightwellstudio.example</li></ul></div>
  <div class="fcol" style="left:880px"><h4>Hours</h4><ul><li>9:00am - 7:00 Pm</li><li>Monday-Friday</li></ul></div>
  <div class="legal"><span>© 2025 Brightwell. All Right Reserved</span><span>FAQs &nbsp;|&nbsp; Privacy Policy &nbsp;|&nbsp; Terms of Service</span></div>
</footer>

</body>
</html>
```